KV MOTORS BANNER/SIGN DESIGN

Design a banner sign for outdoor use for KV MOTORS - a premium pre owned vehicle sales center. The size must be 36 feet in width
and 3 feet in height.

Information required: logo (attached)
-PREMIUM PRE-OWEND VEHICLE SALES
- 403.555.0172

perhaps in smaller font: BUY-SELL-TRADE

prefer white background but could possibly do red matching the logo

```html
<!DOCTYPE html>
<html lang="en">
<head>
<meta charset="utf-8">
<title>KV Motors Banner</title>
<link rel="stylesheet" href="https://fonts.googleapis.com/css2?family=Montserrat:wght@600;700;800;900&display=swap">
<style>
  :root {
    --stage: #2b2b2b;
    --white: #ffffff;
    --ink: #141414;
    --red: #f04438;
    --red-right: #e5393a;
    --red-deep: #c62f2b;
    --red-right-alt: #d93234;
  }
  * { margin: 0; padding: 0; box-sizing: border-box; }
  html, body { width: 1200px; height: 900px; overflow: hidden; }
  body {
    background: var(--stage);
    font-family: "Montserrat", Arial, sans-serif;
    position: relative;
  }
  .banner {
    position: absolute;
    left: 68px;
    width: 1063px;
    height: 88px;
    color: var(--white);
  }
  .banner--white { top: 330px; }
  .banner--red { top: 475px; }
  .banner__bg { position: absolute; inset: 0; width: 100%; height: 100%; }
  .brand {
    position: absolute;
    left: 16px;
    top: 0;
    height: 88px;
    display: flex;
    align-items: center;
    gap: 14px;
  }
  .brand__dot {
    width: 56px;
    height: 56px;
    border-radius: 50%;
    border: 5px solid var(--red);
  }
  .banner--red .brand__dot { border-color: var(--white); }
  .brand__name {
    font-weight: 900;
    font-size: 25px;
    letter-spacing: 1px;
    color: var(--ink);
  }
  .tagline {
    position: absolute;
    left: 320px;
    width: 386px;
    top: 9px;
    text-align: center;
    line-height: 1;
    text-transform: uppercase;
  }
  .tagline__top { display: block; font-weight: 600; font-size: 27px; }
  .tagline__main { display: block; font-weight: 700; font-size: 41px; margin-top: 2px; }
  .contact {
    position: absolute;
    left: 742px;
    top: 14px;
    width: 310px;
  }
  .contact__row { display: flex; align-items: center; gap: 8px; }
  .contact__icon { width: 28px; height: 42px; }
  .contact__phone { font-weight: 700; font-size: 35px; line-height: 1; }
  .contact__services {
    display: block;
    margin-top: 6px;
    text-align: right;
    font-weight: 600;
    font-size: 11px;
    letter-spacing: 6.4px;
  }
</style>
</head>
<body>

  <section class="banner banner--white">
    <svg class="banner__bg" viewBox="0 0 1063 88" preserveAspectRatio="none" aria-hidden="true">
      <rect x="0" y="0" width="1063" height="88" fill="var(--red-right)"/>
      <polygon points="0,0 309,0 286,88 0,88" fill="var(--white)"/>
      <polygon points="309,0 330,0 307,88 286,88" fill="var(--red-deep)"/>
      <polygon points="330,0 731,0 708,88 307,88" fill="var(--red)"/>
      <polygon points="731,0 750,0 727,88 708,88" fill="var(--red-deep)"/>
    </svg>
    <div class="brand">
      <span class="brand__dot"></span>
      <span class="brand__name">KV MOTORS</span>
    </div>
    <p class="tagline">
      <span class="tagline__top">Premium Pre-Owned</span>
      <span class="tagline__main">Vehicle Sales</span>
    </p>
    <div class="contact">
      <div class="contact__row">
        <svg class="contact__icon" viewBox="0 0 28 42" aria-hidden="true">
          <rect x="6" y="3" width="17" height="35" rx="3" transform="rotate(12 14 21)" fill="none" stroke="var(--white)" stroke-width="2.4"/>
        </svg>
        <span class="contact__phone">403 555 0172</span>
      </div>
      <span class="contact__services">BUY-SELL-TRADE</span>
    </div>
  </section>

  <section class="banner banner--red">
    <svg class="banner__bg" viewBox="0 0 1063 88" preserveAspectRatio="none" aria-hidden="true">
      <rect x="0" y="0" width="1063" height="88" fill="var(--red-right-alt)"/>
      <polygon points="0,0 309,0 286,88 0,88" fill="var(--red)"/>
      <polygon points="309,0 330,0 307,88 286,88" fill="var(--red-deep)"/>
      <polygon points="330,0 731,0 708,88 307,88" fill="var(--red)"/>
      <polygon points="731,0 750,0 727,88 708,88" fill="var(--red-deep)"/>
    </svg>
    <div class="brand">
      <span class="brand__dot"></span>
      <span class="brand__name">KV MOTORS</span>
    </div>
    <p class="tagline">
      <span class="tagline__top">Premium Pre-Owned</span>
      <span class="tagline__main">Vehicle Sales</span>
    </p>
    <div class="contact">
      <div class="contact__row">
        <svg class="contact__icon" viewBox="0 0 28 42" aria-hidden="true">
          <rect x="6" y="3" width="17" height="35" rx="3" transform="rotate(12 14 21)" fill="none" stroke="var(--white)" stroke-width="2.4"/>
        </svg>
        <span class="contact__phone">403 555 0172</span>
      </div>
      <span class="contact__services">BUY-SELL-TRADE</span>
    </div>
  </section>

</body>
</html>
```